Web Site Design

We need to design the whole web site for our small start up. We sell hospitality and culinary art internships abroad. I did my own design with WIX which is horrible meanwhile I started with my business. You can see it www.brindle-passage.org I will need you to create a new and attractive web site and to leave it working on wix. The internship destinations are United Arab Emirates, Thailand, China, Spain, Brazil and maybe leave a couple of pages for future destinations.You could also get other ideas of other sites that do internships.

Target Market(s)

Students and recent graduates of hospitality and culinary art majors

Industry/Entity Type

Education

Number of Pages Required

5+ page

Requirements
Must have
• Addittional to our program destinations, or to the pages in the current site. The website must contain a page for Universities or Hotels who require our service

```html
<!DOCTYPE html>
<html lang="en">
<head>
<meta charset="utf-8">
<title>Hospitality Internships</title>
<link rel="stylesheet" href="https://fonts.googleapis.com/css2?family=Josefin+Sans:wght@400;600&family=EB+Garamond:wght@400&display=swap">
<style>
:root{
  --rust:#8b3a10;
  --rust-bright:#a8480f;
  --amber:#c97a2a;
  --wine:#3a0f0c;
  --wine-deep:#1c0806;
  --blush:#d8bdb2;
  --blush-soft:#dcc4ba;
  --ink:#3b2a24;
  --ink-soft:#7a655d;
  --cream:#ffffff;
  --footer:#2a1a15;
}
*{margin:0;padding:0;box-sizing:border-box}
html,body{width:1200px;height:2995px;overflow:hidden}
body{position:relative;background:var(--cream);font-family:"EB Garamond",Georgia,serif;color:var(--ink)}
.abs{position:absolute}
.heading{font-family:"Josefin Sans",Arial,sans-serif;font-weight:400;text-transform:uppercase;letter-spacing:1px}

/* header */
.header{left:0;top:0;width:1200px;height:760px;
  background:linear-gradient(90deg,#5a2a14 0%,#b5621e 4%,#3a1a10 8%,#6b3a1d 50%,#c0752a 93%,#4a2a1e 100%)}
.nav-bar{left:0;top:28px;width:1200px;height:96px;background:var(--rust);box-shadow:0 2px 6px rgba(0,0,0,.35)}
.nav{left:0;top:74px;width:1200px;height:30px}
.nav a{position:absolute;top:0;color:var(--cream);text-decoration:none;font-family:"Josefin Sans",Arial,sans-serif;font-size:18px;letter-spacing:.5px}
.hero-photo{left:44px;top:124px;width:1076px;height:636px;
  background:linear-gradient(90deg,#8a4a1c 0%,#c98a3c 18%,#e8c690 32%,#f1e2c6 45%,#d6b48a 60%,#3a2a2a 75%,#c9a07a 100%)}
.hero-caption{left:576px;top:390px;width:544px;height:180px;background:rgba(55,45,45,.72);padding:26px 14px}
.hero-caption h1{font-family:"Josefin Sans",Arial,sans-serif;font-weight:400;font-size:38px;line-height:50px;color:var(--cream)}
.hero-caption p{font-family:"Josefin Sans",Arial,sans-serif;font-size:25px;letter-spacing:1.5px;color:var(--cream);text-transform:uppercase;margin-top:2px}

/* feature */
.feature{left:0;top:766px;width:1200px;height:664px;
  background:linear-gradient(90deg,#2a0806 0%,#4a120c 30%,#6a1a10 55%,#3a0c08 80%,#7a2a18 100%)}
.feature-band{left:0;top:892px;width:1200px;height:432px;background:rgba(20,6,5,.72)}
.feature h2,.feature-title{left:48px;top:918px;font-size:36px;color:var(--cream)}
.feature-text{left:48px;top:980px;width:510px;font-size:17px;line-height:28.6px;color:#f1e6e0}
.read-more{left:400px;top:1216px;width:146px;text-align:right;font-family:"Josefin Sans",Arial,sans-serif;font-weight:600;font-size:17px;color:var(--cream);letter-spacing:.5px}
.feature-photo{left:596px;top:924px;width:526px;height:364px;border:2px solid #eee;
  background:linear-gradient(90deg,#f0eeea 0%,#d8d6d2 35%,#2a2426 60%,#c63a6a 72%,#1e1a1c 100%)}
.accent-line{left:0;width:1200px;background:var(--rust-bright)}

/* columns */
.columns{left:0;top:1436px;width:1200px;height:494px;background:var(--blush-soft)}
.columns-photo{left:600px;top:1436px;width:600px;height:494px;
  background:linear-gradient(180deg,rgba(230,214,206,.0),rgba(214,192,182,.6)),linear-gradient(90deg,#d6c0b6,#c7ada2 60%,#b8998c)}
.col-title{font-size:36px;color:var(--ink)}
.col-sub{font-size:22px;color:var(--ink)}
.col-text{width:520px;font-size:16px;line-height:26px;color:var(--ink-soft)}

/* expertise */
.expertise{left:0;top:1930px;width:1200px;height:566px;background:var(--blush)}
.expertise-title{left:52px;top:1980px;font-size:40px;color:var(--ink)}
.expertise-photo{left:44px;top:2060px;width:526px;height:360px;
  background:linear-gradient(180deg,#f2a640 0%,#c9742a 40%,#3a2a22 62%,#d8a050 75%,#2a201c 100%)}
.quote{left:636px;top:2290px;font-size:22px;line-height:46px;color:var(--ink)}

/* footer */
.footer{left:0;top:2520px;width:1200px;height:475px;
  background:linear-gradient(180deg,#33221b 0%,#2a1a15 60%,#241612 100%)}
.footer-title{top:2596px;font-size:24px;color:var(--cream)}
.footer-blurb{left:50px;top:2678px;width:250px;font-size:14px;line-height:18px;color:#efe5e0}
.footer-list{list-style:none;font-size:19px;line-height:35px;color:#efe5e0}
.footer-contact{left:952px;top:2670px;width:230px;font-size:19px;line-height:29px;color:#efe5e0}
</style>
</head>
<body>

<div class="abs header" role="img" aria-label="Warm-lit hotel exterior backdrop"></div>
<div class="abs nav-bar"></div>
<nav class="abs nav">
  <a style="left:506px">HOME</a>
  <a style="left:590px">SERVICES</a>
  <a style="left:702px">DESTINATIONS</a>
  <a style="left:850px">ABOUT</a>
  <a style="left:938px">CONTACT</a>
</nav>
<div class="abs hero-photo" role="img" aria-label="Hotel receptionist holding a tablet in an elegant lobby"></div>
<div class="abs hero-caption">
  <h1>Hospitality internships<br>are our specialty!</h1>
  <p>Quod permitit lumen</p>
</div>

<section>
  <div class="abs feature" role="img" aria-label="Dark red dining table backdrop with dates and woven cloth"></div>
  <div class="abs feature-band"></div>
  <h2 class="abs heading feature-title">Erit nihil</h2>
  <p class="abs feature-text">Quisque tincidunt quam a porta sagittis. Etiam at urna dolor. Curabitur semper, arcu ut consequat sagittis, arcu purus venenatis est, et tristique nibh nibh porttitor odio. Nunc blandit ac ante in accumsan. Vestibulum ac tincidunt eros. Suspendisse elementum in nisi ut fringilla. Suspendisse tincidunt orci sit amet tellus porta placerat. Nunc sed turpis ullamcorper, cursus sapien a, placerat massa. Duis auctor eleifend est, et maximus est sagittis vel. In sit</p>
  <a class="abs read-more">READ MORE</a>
  <div class="abs feature-photo" role="img" aria-label="Room service attendant carrying a breakfast tray"></div>
</section>

<div class="abs accent-line" style="top:1430px;height:6px"></div>

<section>
  <div class="abs columns"></div>
  <div class="abs columns-photo" role="img" aria-label="Faded hotel room interior"></div>
  <h2 class="abs heading col-title" style="left:42px;top:1532px">Etiam at quoque</h2>
  <p class="abs col-text" style="left:42px;top:1590px">Quisque tincidunt quam a porta sagittis. Etiam at urna dolor. Curabitur semper, arcu ut consequat sagittis, arcu purus venenatis est, et tristique nibh nibh porttitor odio. Nunc blandit ac ante in accumsan. Vestibulum ac tincidunt eros. Suspendisse elementum in nisi ut fringilla. Suspendisse tincidunt orci sit amet tellus porta</p>
  <h3 class="abs heading col-sub" style="left:42px;top:1756px">Et quique potest</h3>
  <p class="abs col-text" style="left:42px;top:1806px">Quisque tincidunt quam a porta sagittis. Etiam at urna dolor. Curabitur semper, arcu ut consequat sagittis, arcu purus venenatis est, et tristique nibh nibh porttitor odio. Nunc blandit ac ante in</p>

  <h2 class="abs heading col-title" style="left:630px;top:1524px">Percit tuta</h2>
  <p class="abs col-text" style="left:630px;top:1584px">Quisque tincidunt quam a porta sagittis. Etiam at urna dolor. Curabitur semper, arcu ut consequat sagittis, arcu purus venenatis est, et tristique nibh nibh porttitor odio. Nunc blandit ac ante in accumsan. Vestibulum ac tincidunt eros. Suspendisse elementum in nisi ut fringilla. Suspendisse tincidunt orci sit amet tellus porta</p>
  <h3 class="abs heading col-sub" style="left:630px;top:1748px">Et comprehenda</h3>
  <p class="abs col-text" style="left:630px;top:1798px">Quisque tincidunt quam a porta sagittis. Etiam at urna dolor. Curabitur semper, arcu ut consequat sagittis, arcu purus venenatis est, et tristique nibh nibh porttitor odio. Nunc blandit ac ante in</p>
</section>

<section>
  <div class="abs expertise"></div>
  <h2 class="abs heading expertise-title">Our expertise</h2>
  <div class="abs expertise-photo" role="img" aria-label="Illuminated hotel facade with a lit sign at dusk"></div>
  <h3 class="abs heading col-sub" style="left:636px;top:2100px">Vulpus elit</h3>
  <p class="abs col-text" style="left:636px;top:2156px;width:560px">Quisque tincidunt quam a porta sagittis. Etiam at urna dolor. Curabitur semper, arcu ut consequat sagittis, arcu purus venenatis est, et tristique nibh nibh porttitor odio. Nunc blandit ac ante in</p>
  <blockquote class="abs quote">“eternatitem magistima chose<br>perception randa quod vivendum<br>et se quanda scit…”</blockquote>
</section>

<div class="abs accent-line" style="top:2496px;height:24px;background:var(--rust)"></div>

<footer>
  <div class="abs footer" role="img" aria-label="Dim hotel facade backdrop"></div>
  <p class="abs footer-blurb">Phasellus vulputate et nisi a luctus. Curabitur vitae nunc viverra, fermentum dui in, vehicula velit. Pellentesque habitant morbi tristique senectus et netus et malesuada fames ac turpis egestas. Suspendisse lacinia commodo libero in vestibulum. Aenean mattis dictum felis, eu commodo arcu tincidunt nec. Fusce rhoncus eros sed ante pulvinar sagittis. Fusce facilisis</p>

  <h4 class="abs heading footer-title" style="left:340px">Services</h4>
  <ul class="abs footer-list" style="left:334px;top:2672px">
    <li>Phasellus vulputate</li><li>Enisi a luctus.</li><li>Curabitur vitae nunc</li><li>Viverra, fermentum</li><li>Dui in, vehicula velit.</li><li>Pellentesque habitant</li><li>Senectus et netus et</li><li>Malesuada fames ac</li>
  </ul>

  <h4 class="abs heading footer-title" style="left:626px">More links</h4>
  <ul class="abs footer-list" style="left:626px;top:2672px">
    <li>Phasellus vulputate</li><li>Enisi a luctus.</li><li>Curabitur vitae nunc</li><li>Viverra, fermentum</li><li>Dui in, vehicula velit.</li><li>Pellentesque habitant</li><li>Senectus et netus et</li><li>Malesuada fames ac</li>
  </ul>

  <h4 class="abs heading footer-title" style="left:916px">Contact us</h4>
  <address class="abs footer-contact" style="font-style:normal">Address:<br>Phasellus vulputate et nisi a luctus. Curabitur vitae nunc viverra, fermentum dui in, vehicula velit. Pellentesque habitant morbi tristique senectus et netus et malesuada fames ac turpis egestas.</address>
</footer>

</body>
</html>
```